Boat business cards

I'm looking for business cards with the two logos I've attached. I don't have an specific idea in mind and open to anything. All the usual info will be on the card. Name, position in company, nr, email, address, ect. The company rents out these two boats for charters and fishing.

```html
<!DOCTYPE html>
<html lang="en">
<head>
<meta charset="utf-8">
<title>Boat Charter Business Cards</title>
<link href="https://fonts.googleapis.com/css2?family=Jost:wght@400;500&display=swap" rel="stylesheet">
<style>
  :root {
    --page: #eef1f6;
    --paper: #ffffff;
    --navy: #1f4f98;
    --navy-deep: #17397a;
    --teal: #22b3c4;
    --ink: #133b73;
    --edge: #9aa3b0;
    --text-light: #ffffff;
  }
  * { margin: 0; padding: 0; box-sizing: border-box; }
  html, body {
    width: 1200px; height: 504px; overflow: hidden;
    background: var(--page);
    font-family: "Jost", "Futura", sans-serif;
  }
  .sheet { position: relative; width: 1200px; height: 504px; }
  .card {
    position: absolute; top: 102px;
    width: 526px; height: 300px;
    background: var(--paper);
    border: 1px solid var(--edge);
    overflow: hidden;
  }
  .card--front { left: 50px; }
  .card--back { left: 624px; }
  .card__waves { position: absolute; inset: 0; width: 100%; height: 100%; }

  .brand {
    position: absolute;
    display: flex; align-items: center; gap: 7px;
    color: var(--ink); font-weight: 500; white-space: nowrap;
  }
  .brand__dot { display: block; border-radius: 50%; background: var(--ink); }
  .brand--small { top: 58px; right: 56px; font-size: 19px; }
  .brand--small .brand__dot { width: 10px; height: 10px; }
  .brand--large { top: 160px; left: 0; right: 0; justify-content: center; font-size: 38px; }
  .brand--large .brand__dot { width: 16px; height: 16px; }

  .holder { position: absolute; left: 62px; top: 108px; }
  .holder__name { font-size: 25px; font-weight: 400; color: var(--ink); letter-spacing: 0.3px; line-height: 1; }
  .holder__name span { color: var(--teal); }
  .holder__role { font-size: 13px; color: var(--ink); margin-top: 4px; }

  .contact {
    position: absolute; left: 58px; right: 40px; top: 218px;
    display: grid; grid-template-columns: 1fr 1fr;
    row-gap: 20px; column-gap: 60px;
    color: var(--text-light); font-size: 13px;
  }
  .contact__item { display: flex; align-items: center; gap: 6px; }
  .contact__item:nth-child(even) { padding-left: 6px; }
  .contact__icon { width: 11px; height: 11px; flex: none; }
  .contact__divider {
    position: absolute; left: 262px; top: 222px;
    width: 2px; height: 50px; background: var(--text-light);
  }
</style>
</head>
<body>
<main class="sheet">

  <section class="card card--front">
    <svg class="card__waves" viewBox="0 0 526 300" aria-hidden="true">
      <defs>
        <linearGradient id="front-sea" x1="0" y1="0" x2="1" y2="1">
          <stop offset="0" stop-color="#2160a8"/>
          <stop offset="1" stop-color="#1c3f86"/>
        </linearGradient>
      </defs>
      <path d="M0,140 C70,172 160,188 265,170 C365,152 445,104 526,64 L526,300 L0,300 Z" fill="url(#front-sea)"/>
      <path d="M0,156 C80,186 170,196 275,178 C370,160 450,110 526,72" fill="none" stroke="var(--teal)" stroke-width="7"/>
      <path d="M0,147 C75,178 165,190 268,173 C366,156 446,107 526,67" fill="none" stroke="#fff" stroke-width="2.5"/>
      <path d="M0,166 C85,196 180,204 285,186 C375,170 452,118 526,80" fill="none" stroke="#fff" stroke-width="1.5"/>
    </svg>

    <div class="brand brand--small"><span class="brand__dot"></span>Polar Tide</div>

    <div class="holder">
      <h1 class="holder__name">YOUR <span>NAME</span></h1>
      <p class="holder__role">Position In Company</p>
    </div>

    <div class="contact__divider"></div>
    <ul class="contact">
      <li class="contact__item">
        <svg class="contact__icon" viewBox="0 0 12 12"><path d="M2.5 1 L4.5 1 L5.2 3.6 L4 4.6 C4.7 6 6 7.3 7.4 8 L8.4 6.8 L11 7.5 L11 9.5 C11 10.3 10.3 11 9.5 11 C5 11 1 7 1 2.5 C1 1.7 1.7 1 2.5 1 Z" fill="var(--teal)"/></svg>
        XXX XXX XXX
      </li>
      <li class="contact__item">
        <svg class="contact__icon" viewBox="0 0 12 12"><path d="M6 0.5 C3.8 0.5 2.2 2.1 2.2 4.2 C2.2 7 6 11.5 6 11.5 C6 11.5 9.8 7 9.8 4.2 C9.8 2.1 8.2 0.5 6 0.5 Z M6 5.6 A1.4 1.4 0 1 1 6 2.8 A1.4 1.4 0 1 1 6 5.6 Z" fill="var(--teal)"/></svg>
        Your Address
      </li>
      <li class="contact__item">
        <svg class="contact__icon" viewBox="0 0 12 12"><rect x="1" y="2.5" width="10" height="7" fill="none" stroke="var(--teal)" stroke-width="1.2"/><path d="M1 2.5 L6 6.5 L11 2.5" fill="none" stroke="var(--teal)" stroke-width="1.2"/></svg>
        Youremail@mail.com
      </li>
      <li class="contact__item">
        <svg class="contact__icon" viewBox="0 0 12 12"><circle cx="6" cy="6" r="5" fill="none" stroke="var(--teal)" stroke-width="1.2"/><path d="M1 6 H11 M6 1 C3.5 3.5 3.5 8.5 6 11 M6 1 C8.5 3.5 8.5 8.5 6 11" fill="none" stroke="var(--teal)" stroke-width="1"/></svg>
        Your Website
      </li>
    </ul>
  </section>

  <section class="card card--back">
    <svg class="card__waves" viewBox="0 0 526 300" aria-hidden="true">
      <defs>
        <linearGradient id="back-sea" x1="0" y1="0" x2="1" y2="0">
          <stop offset="0" stop-color="#2160a8"/>
          <stop offset="1" stop-color="#1c3f86"/>
        </linearGradient>
      </defs>
      <path d="M0,173 C90,212 210,258 340,268 C430,274 485,266 526,256 L526,300 L0,300 Z" fill="url(#back-sea)"/>
      <path d="M150,228 C260,268 420,276 526,254" fill="none" stroke="#fff" stroke-width="3"/>
      <path d="M160,236 C265,274 425,282 526,262" fill="none" stroke="var(--teal)" stroke-width="6"/>
    </svg>

    <div class="brand brand--large"><span class="brand__dot"></span>Sea Breeze</div>
  </section>

</main>
</body>
</html>
```